International Food Manufacturer in the need of a new business card and logo.

Our Company - Northgate Pantry Ltd.

Our Industry - Food and Drink

We are a Wild Harvested Food Distributor / Manufacturer. We service the following food sectors: Supermarkets, Hotels, Restaurants, Cafes, Catering and all people looking to eat healthy food products.

Slogan - Pure wild flavour for every healthy table

Business card details -

48-52 Marlow Lane
Hatherby Green
London
EC9Z 4RT United Kingdom
Dennis Prowle
+44 7000 481736 - UK
+971 50 7739205 - UAE
+38 063 914 2758 - Ukraine
dennis@northgatepantry.example
www.northgatepantry.example

Goal - We are looking for a dynamic modern new look for our corporate image and a designer who can bring this new concept to our future food product designs. Please try to incorporate 3d hexagonal vector Imaging in your design concepts.

Target Market(s)

Industry/Entity Type

Food Service

Contact Information for Business Card

Northgate Pantry Ltd.
48-52 Marlow Lane
Hatherby Green
London
EC9Z 4RT United Kingdom
Dennis Prowle
+44 7000 481736 - UK
+971 50 7739205 - UAE

Font styles to use
Serif

Colors

Designer to choose colors to be used in the design.

Requirements
Must have
• Please read project description above.
Nice to have
Should not have

```html
<!DOCTYPE html>
<html lang="en">
<head>
<meta charset="utf-8">
<title>Northgate Pantry Ltd. — Business Card</title>
<link rel="stylesheet" href="https://fonts.googleapis.com/css2?family=Arimo:wght@400;700&family=Tinos&display=swap">
<style>
  :root {
    --page-bg: #e6e4e0;
    --card-dark: #262626;
    --card-mid: #3c3c3c;
    --card-light: #555555;
    --text-light: #f1f1f1;
    --text-soft: #d4d4d4;
    --rule: #bdbdbd;
    --band-light: #f4f4f4;
    --band-shade: #c6c6c6;
    --band-text: #555555;
  }
  * { box-sizing: border-box; margin: 0; padding: 0; }
  html, body {
    width: 1200px; height: 1023px; overflow: hidden;
    background: var(--page-bg);
  }
  .card {
    position: absolute; left: 120px; top: 237px;
    width: 960px; height: 549px;
    border-radius: 20px; overflow: hidden;
    background:
      radial-gradient(ellipse 60% 80% at 30% 35%, rgba(255,255,255,0.16), rgba(255,255,255,0) 70%),
      linear-gradient(160deg, var(--card-light) 0%, var(--card-mid) 45%, var(--card-dark) 100%);
    box-shadow: 0 12px 30px rgba(0,0,0,0.25);
    font-family: "Arimo", Arial, sans-serif;
    color: var(--text-light);
  }
  .company-name {
    position: absolute; left: 64px; top: 408px;
    font-family: "Tinos", "Times New Roman", serif;
    font-size: 25px; letter-spacing: 1.5px; text-transform: uppercase;
    color: var(--text-soft);
  }
  .divider {
    position: absolute; left: 478px; top: 64px;
    width: 1px; height: 380px; background: var(--rule);
  }
  .contact { position: absolute; left: 512px; top: 58px; }
  .person-name {
    font-size: 40px; font-weight: 700; letter-spacing: 0.5px;
    text-transform: uppercase; line-height: 1;
  }
  .person-role {
    font-size: 15px; letter-spacing: 1px; text-transform: uppercase;
    color: var(--text-soft); margin-top: 6px;
  }
  .address { margin-top: 14px; font-size: 20px; line-height: 27px; color: var(--text-soft); }
  .channels { margin-top: 18px; list-style: none; font-size: 20px; line-height: 28px; color: var(--text-soft); }
  .channels li { display: flex; align-items: center; gap: 12px; }
  .channels svg { width: 15px; height: 15px; fill: var(--text-soft); flex: none; }
  .slogan-band {
    position: absolute; left: 0; bottom: 0; width: 100%; height: 54px;
    background: linear-gradient(180deg, var(--band-light) 0%, #e2e2e2 60%, var(--band-shade) 100%);
    display: flex; align-items: center; justify-content: flex-end; padding-right: 52px;
  }
  .slogan {
    font-size: 19px; letter-spacing: 1.6px; text-transform: uppercase;
    color: var(--band-text); white-space: nowrap;
  }
</style>
</head>
<body>
  <div class="card">
    <div class="company-name">Northgate Pantry Ltd.</div>
    <div class="divider"></div>
    <div class="contact">
      <div class="person-name">Harlan Vossberg</div>
      <div class="person-role">Director</div>
      <div class="address">
        48-52 Marlow Lane<br>
        Hatherby Green London<br>
        EC9Z 4RT United Kingdom<br>
        Dennis Prowle
      </div>
      <ul class="channels">
        <li><svg viewBox="0 0 16 16" aria-hidden="true"><path d="M3.5 1l3 3-1.8 1.8a9 9 0 0 0 5.5 5.5L12 9.5l3 3-2 2.5C7 14.5 1.5 9 1 3z"/></svg>+44 7000 481736 - UK</li>
        <li><svg viewBox="0 0 16 16" aria-hidden="true"><path d="M4 0h8a1 1 0 0 1 1 1v14a1 1 0 0 1-1 1H4a1 1 0 0 1-1-1V1a1 1 0 0 1 1-1zm1 2v10h6V2z"/></svg>+971 50 7739205 - UAE</li>
        <li><svg viewBox="0 0 16 16" aria-hidden="true"><path d="M8 1C4 1 1 3.7 1 7c0 1.8.9 3.3 2.3 4.4L2.5 15l3.8-2.2c.5.1 1.1.2 1.7.2 4 0 7-2.7 7-6S12 1 8 1z"/></svg>+38 063 914 2758 - Ukraine</li>
        <li><svg viewBox="0 0 16 16" aria-hidden="true"><path d="M1 3h14v10H1zm1.5 1.5L8 9l5.5-4.5v-.2h-11z"/></svg>dennis@northgatepantry.example</li>
        <li><svg viewBox="0 0 16 16" aria-hidden="true"><path d="M8 1a7 7 0 1 0 0 14A7 7 0 0 0 8 1zm-1 1.6C5.8 4 5.2 5.8 5.1 7.3H2.6A5.5 5.5 0 0 1 7 2.6zm2 0a5.5 5.5 0 0 1 4.4 4.7h-2.5C10.8 5.8 10.2 4 9 2.6zM6.6 7.3C6.7 5.8 7.2 4.4 8 3.3c.8 1.1 1.3 2.5 1.4 4zM2.6 8.7h2.5c.1 1.5.7 3.3 1.9 4.7a5.5 5.5 0 0 1-4.4-4.7zm4 0h2.8c-.1 1.5-.6 2.9-1.4 4-.8-1.1-1.3-2.5-1.4-4zm4.3 0h2.5A5.5 5.5 0 0 1 9 13.4c1.2-1.4 1.8-3.2 1.9-4.7z"/></svg>www.northgatepantry.example</li>
      </ul>
    </div>
    <div class="slogan-band">
      <span class="slogan">Pure wild flavour for every healthy table</span>
    </div>
  </div>
</body>
</html>
```